Narvelo - Human Capital Consultancy Business Cards

We need a business card design for a new professional services consulting company which is focused on People, Performance, Profit. Hence the company name "Narvelo Pty Ltd". We intend to work with organisations predominantly on achieving optimal business performance through it's people. Developing both individual and organisational capability through effective learning and talent management strategies. We also plan to offer leadership programs which look at how people can utilise wellness, mindfulness and resilience to enable them and their teams to perform more effectively. We are looking for something quite dynamic, even sporty looking rather than a staid'professional services' look. Please see logo attached.

Leadership

```html
<!DOCTYPE html>
<html lang="en">
<head>
<meta charset="utf-8">
<title>Narvelo Pty Ltd – Business Cards</title>
<link rel="stylesheet" href="https://fonts.googleapis.com/css2?family=Open+Sans:wght@400;600;700&display=swap">
<style>
  :root {
    --page-bg: #e9eaec;
    --white: #ffffff;
    --paper: #f4f4f4;
    --logo-grey: #5d6470;
    --accent-red: #e52a2a;
    --accent-orange: #f5a21c;
    --name-gold: #f6b21a;
    --blue-deep: #2a37a8;
    --blue-mid: #2b78d2;
    --blue-cyan: #2fb4e4;
    --text-light: #eaf4ff;
  }
  * { box-sizing: border-box; margin: 0; padding: 0; }
  html, body {
    width: 1200px; height: 1023px; overflow: hidden;
    background: var(--page-bg);
    font-family: "Open Sans", Arial, sans-serif;
  }
  .sheet {
    width: 1200px; height: 1023px;
    display: flex; flex-direction: column; align-items: center; justify-content: center;
    gap: 36px;
  }
  .card {
    position: relative; width: 800px; height: 457px;
    border-radius: 26px; overflow: hidden;
    box-shadow: 0 6px 18px rgba(0,0,0,.18);
  }

  /* Front */
  .card-front { background: linear-gradient(35deg, var(--blue-cyan) 0%, var(--blue-mid) 55%, var(--blue-deep) 100%); }
  .card-front .band { position: absolute; inset: 0; width: 100%; height: 100%; }
  .brand-name {
    position: absolute; left: 44px; top: 42px;
    font-weight: 700; font-size: 58px; letter-spacing: 2px; line-height: 1;
    color: var(--logo-grey);
  }
  .brand-tagline {
    position: absolute; left: 46px; top: 112px;
    font-size: 21px; color: var(--logo-grey); letter-spacing: .5px;
  }
  .holder { position: absolute; right: 40px; top: 160px; text-align: right; color: var(--text-light); }
  .holder-name { font-weight: 700; font-size: 30px; color: var(--name-gold); line-height: 1.1; }
  .holder-title { font-size: 16px; margin-top: 2px; }
  .holder-company { font-weight: 700; font-size: 15px; margin-top: 24px; letter-spacing: .5px; }
  .holder-address { font-size: 16px; line-height: 1.35; }
  .contact { position: absolute; left: 44px; bottom: 34px; list-style: none; color: var(--text-light); font-size: 16px; }
  .contact li { display: flex; align-items: center; gap: 12px; line-height: 25px; }
  .contact svg { width: 16px; height: 16px; fill: none; stroke: var(--text-light); stroke-width: 1.6; }

  /* Back */
  .card-back { background: radial-gradient(ellipse at 52% 50%, var(--blue-cyan) 0%, var(--blue-mid) 45%, var(--blue-deep) 100%); }
  .back-tagline { position: absolute; left: 40px; top: 36px; color: var(--white); font-size: 28px; font-weight: 600; letter-spacing: .5px; }
  .back-url { position: absolute; left: 42px; top: 84px; color: var(--text-light); font-size: 16px; }
  .back-brand {
    position: absolute; left: 50%; top: 54%; transform: translate(-50%, -50%);
    color: var(--white); font-weight: 700; font-size: 84px; letter-spacing: 2px; line-height: 1;
  }
</style>
</head>
<body>
<main class="sheet">
  <section class="card card-front" aria-label="Business card front">
    <svg class="band" viewBox="0 0 800 457" preserveAspectRatio="none" aria-hidden="true">
      <polygon points="0,0 800,0 800,110 0,190" fill="var(--paper)"/>
      <polygon points="0,190 800,110 800,118 0,200" fill="var(--accent-red)"/>
      <polygon points="0,200 800,118 800,122 0,204" fill="var(--accent-orange)"/>
    </svg>
    <p class="brand-name">NARVELO</p>
    <p class="brand-tagline">Growth • Focus • Results</p>

    <div class="holder">
      <p class="holder-name">Daniel Harper</p>
      <p class="holder-title">President &amp; CEO</p>
      <p class="holder-company">NARVELO PTY LTD.</p>
      <p class="holder-address">Somewhere Streetname Address<br>Cityname, CN 12345</p>
    </div>

    <ul class="contact">
      <li><svg viewBox="0 0 16 16"><path d="M3 2h3l1 3-2 1c1 2 2 3 4 4l1-2 3 1v3c-6 0-10-4-10-10z"/></svg>+1 555 018 2290</li>
      <li><svg viewBox="0 0 16 16"><rect x="4" y="1" width="8" height="14" rx="1.5"/><line x1="7" y1="12.5" x2="9" y2="12.5"/></svg>+1 555 017 6614</li>
      <li><svg viewBox="0 0 16 16"><rect x="2" y="6" width="12" height="8" rx="1"/><rect x="4" y="2" width="8" height="4"/></svg>+1 555 019 7702</li>
      <li><svg viewBox="0 0 16 16"><rect x="1.5" y="3.5" width="13" height="9" rx="1"/><polyline points="1.5,4 8,9 14.5,4"/></svg>dharper@narvelo.com</li>
      <li><svg viewBox="0 0 16 16"><circle cx="8" cy="8" r="6.5"/><ellipse cx="8" cy="8" rx="3" ry="6.5"/><line x1="1.5" y1="8" x2="14.5" y2="8"/></svg>www.narvelo.com</li>
    </ul>
  </section>

  <section class="card card-back" aria-label="Business card back">
    <p class="back-tagline">Growth • Focus • Results</p>
    <p class="back-url">www.narvelo.com</p>
    <p class="back-brand">NARVELO</p>
  </section>
</main>
</body>
</html>
```